Flyer Design Project

We are a mortgage company Tamberlyn Funding Corp. that will be looking to mail out these flyers to promote Reverse Mortgages. Some clip art of Seniors (Happy Smile having a good time) Our phone number on the flyer in a few places 877-520-6184
Text: No Celebrity Endorsers or talking heads here
Solutions for seniors... Stop worrying Start Living
Say Goodby to monthly payments with a reverse mortgage
The Loan That Pays You
Secure Your Retirement With A Reverse Mortgage
GKP Goverment Insured
Retain Complete ownership of your Home
Save and Effective Financial Tool
Pay Off Credit cards Elimanate Mortgage payments improve your home or lifestyle
No Credit score or income requirements
Faceing a foreclosure a reverse mortgage can help
Is a reverse mortgage right for you? Get the facts from a qualified reverse mortgage originator
The text above does not have to be in that order
I am having trouble with my Logo so i am getting a new file and will be able to upload it to the flyer shortly just leave room for it
Seniors over the age of 62
Financial

```html
<!DOCTYPE html>
<html lang="en">
<head>
<meta charset="utf-8">
<title>Tamberlyn Funding Corp. – Reverse Mortgage Flyer</title>
<link rel="stylesheet" href="https://fonts.googleapis.com/css2?family=Cormorant+Garamond:wght@500&family=Crimson+Text&display=swap">
<style>
  :root {
    --page: #ffffff;
    --plum-deep: #1a0a3a;
    --plum: #2e0f5c;
    --plum-mid: #3d1470;
    --magenta: #e21fc0;
    --magenta-light: #f35bd8;
    --magenta-dark: #a0108a;
    --ink-light: #ffffff;
    --ink-soft: #e4dcf0;
    --photo-light: #f7f1ec;
    --photo-warm: #e8cdbb;
    --photo-skin: #d4a98f;
  }
  * { margin: 0; padding: 0; box-sizing: border-box; }
  html, body { width: 948px; height: 1200px; overflow: hidden; background: var(--page); }
  .flyer {
    position: absolute;
    left: 32px; top: 30px;
    width: 882px; height: 1140px;
    overflow: hidden;
    background: linear-gradient(180deg, var(--plum-mid) 50%, var(--plum-deep) 100%);
  }
  .hero-photo {
    position: absolute;
    left: 0; top: 0;
    width: 882px; height: 640px;
    background: linear-gradient(165deg, var(--photo-warm) 0%, var(--photo-skin) 30%, var(--photo-warm) 55%, var(--photo-light) 80%);
  }
  .wave { position: absolute; left: 0; top: 0; width: 882px; height: 1140px; }
  .headline {
    position: absolute;
    left: 78px; top: 652px;
    font-family: "Cormorant Garamond", "Times New Roman", serif;
    font-weight: 500;
    font-size: 57px;
    line-height: 62px;
    color: var(--ink-light);
  }
  .headline .highlight {
    background: var(--magenta);
    padding: 0 8px 0 4px;
  }
  .benefits {
    position: absolute;
    left: 78px; top: 800px;
    list-style: none;
    font-family: "Crimson Text", "Times New Roman", serif;
    font-size: 19.5px;
    line-height: 23px;
    color: var(--ink-soft);
    white-space: nowrap;
  }
  .benefits .sep { font-size: 12px; vertical-align: 2px; margin: 0 4px; color: var(--ink-light); }
  .call-line {
    position: absolute;
    left: 78px; top: 1010px;
    font-family: "Crimson Text", "Times New Roman", serif;
    font-size: 27px;
    color: var(--ink-light);
    white-space: nowrap;
  }
  .call-line .phone { background: var(--magenta); padding: 0 6px; }
</style>
</head>
<body>
  <main class="flyer">
    <div class="hero-photo" role="img" aria-label="Photograph of an elderly hand gently held by a younger hand on a white background"></div>

    <svg class="wave" viewBox="0 0 882 1140" aria-hidden="true">
      <defs>
        <linearGradient id="magentaBand" x1="0" y1="0" x2="1" y2="0">
          <stop offset="0" stop-color="#a0108a"/>
          <stop offset="0.5" stop-color="#e21fc0"/>
          <stop offset="1" stop-color="#f35bd8"/>
        </linearGradient>
        <linearGradient id="plumBody" x1="0" y1="0" x2="0" y2="1">
          <stop offset="0" stop-color="#4a1680"/>
          <stop offset="0.3" stop-color="#2e0f5c"/>
          <stop offset="1" stop-color="#1a0a3a"/>
        </linearGradient>
      </defs>
      <path d="M0,370 C220,410 430,560 882,470 L882,1140 L0,1140 Z" fill="url(#magentaBand)"/>
      <path d="M0,470 C260,500 470,620 882,540 L882,600 C520,690 260,560 0,520 Z" fill="#f35bd8" opacity="0.55"/>
      <path d="M0,520 C260,560 520,700 882,610 L882,1140 L0,1140 Z" fill="url(#plumBody)"/>
      <path d="M0,540 C280,580 540,720 882,640" fill="none" stroke="#e21fc0" stroke-width="2" opacity="0.5"/>
    </svg>

    <h1 class="headline">Happy <span class="highlight">Smile</span><br>having a good time</h1>

    <ul class="benefits">
      <li>No Celebrity Endorsers or talking heads here</li>
      <li>Solutions for seniors... Stop worrying Start Living<span class="sep">&#9654;</span>GKP Goverment Insured</li>
      <li>Say Goodby to monthly payments with a reverse mortgage</li>
      <li>Secure Your Retirement With A Reverse Mortgage<span class="sep">&#9654;</span>The Loan That Pays You</li>
      <li>Retain Complete ownership of your Home<span class="sep">&#9654;</span>Save and Effective Financial Tool</li>
      <li>Pay Off Credit cards Elimanate Mortgage payments improve your home or lifestyle</li>
      <li>No Credit score or income requirement<span class="sep">&#9654;</span>Faceing a foreclosure a reverse mortgage can help</li>
      <li>Is a reverse mortgage right for you? Get the facts from a qualified reverse mortgage originator</li>
    </ul>

    <p class="call-line">Our phone number on the flyer in a few places <span class="phone">877-520-6184</span></p>
  </main>
</body>
</html>
```